Harrowgate Legal

To update and modernize current business card appearance. Marisa's business is based in Melbourne with 4 other lawyers in the firm. Marisa travels to the Pilbara in Western Australia approximately 1 week a month as part of the firms legal work. She consults with clients in Newman, Tom Price and Port Hedland. The lawyers work mostly from a home office, apart from court appearances. They have a virtual office in Melbourne city, and use facilities in 3 or 4 other locations around Melbourne. It is important the client's think this is a conventional law firm with a permanent office. Our business structure is a difficult concept for them to grasp. The business has been operational for 3 years, growing from 1 lawyer to 4 lawyers during that time. Our website is www.Harrowgatelegal.com.au and is currently being upgraded as we are not happy with its content. The logo is currently orange and dark grey but the orange is a difficult colour to reproduce and often turns out "poo" brown when documents are printed. We need clients to know we are user friendly and caring - and not head up our rears ends as some lawyers appear to be.
Updates

Thank you for the feedback so far. 1. Some of the designs have too much black (We prefer darker grey & not too much.) 2. Happy for designers to play around with different colours & logo design. What we're after is a modern look and business card that people say "wow" when they pick it up.

Industry/Entity Type

Business

```html
<!DOCTYPE html>
<html lang="en">
<head>
<meta charset="utf-8">
<title>Harrowgate Legal – Business Card</title>
<link rel="stylesheet" href="https://fonts.googleapis.com/css2?family=Open+Sans:wght@400;600;700&display=swap">
<style>
  :root {
    --stage: #c9c9c9;
    --stage-light: #d9d9d9;
    --charcoal: #3b3b3b;
    --charcoal-dark: #2e2e2e;
    --charcoal-light: #4a4a4a;
    --orange: #f26a1b;
    --white: #ffffff;
    --ink: #4a4a4a;
    --muted: #d6d6d6;
  }
  * { box-sizing: border-box; margin: 0; padding: 0; }
  html, body { width: 1200px; height: 900px; overflow: hidden; }
  body {
    background: radial-gradient(ellipse at 50% 40%, var(--stage-light), var(--stage) 75%);
    font-family: "Open Sans", sans-serif;
    position: relative;
  }
  .card {
    position: absolute;
    top: 300px;
    width: 520px;
    height: 300px;
    border-radius: 22px;
    overflow: hidden;
    box-shadow: 0 10px 26px rgba(0,0,0,0.25);
  }
  .card-textured {
    background: linear-gradient(160deg, var(--charcoal-light), var(--charcoal) 45%, var(--charcoal-dark));
  }

  /* Back of card */
  .card-back { left: 65px; color: var(--white); text-align: center; }
  .practice-heading {
    margin-top: 30px;
    color: var(--orange);
    font-weight: 700;
    font-size: 20px;
    letter-spacing: 0.3px;
  }
  .practice-list { list-style: none; margin-top: 24px; }
  .practice-area { margin-bottom: 20px; }
  .practice-title { font-weight: 700; font-size: 17px; }
  .practice-title::before { content: "• "; color: var(--orange); }
  .practice-detail { font-size: 12px; line-height: 1.3; color: var(--muted); }
  .service-region {
    color: var(--orange);
    font-weight: 700;
    font-size: 15px;
    line-height: 1.3;
    margin-top: 10px;
  }
  .website {
    position: absolute;
    left: 32px;
    bottom: 22px;
    font-size: 15px;
    font-weight: 600;
    letter-spacing: 4.6px;
  }

  /* Front of card */
  .card-front { left: 615px; background: var(--white); }
  .front-top {
    position: relative;
    height: 158px;
    background: var(--white);
  }
  .brand {
    position: absolute;
    left: 32px;
    top: 58px;
    display: flex;
    align-items: center;
    gap: 10px;
  }
  .brand-dot {
    width: 26px; height: 26px;
    border-radius: 50%;
    background: var(--orange);
  }
  .brand-name {
    color: var(--ink);
    font-weight: 600;
    font-size: 28px;
    letter-spacing: 0.5px;
  }
  .values {
    position: absolute;
    right: 48px;
    top: 54px;
    list-style: none;
    font-size: 10px;
    color: var(--ink);
    text-transform: uppercase;
  }
  .values li { margin-bottom: 26px; }
  .values li::before { content: "• "; color: var(--orange); }
  .accent-rule { height: 7px; background: var(--orange); }
  .front-bottom {
    height: 135px;
    padding: 14px 0 0 30px;
    color: var(--white);
  }
  .person-name { color: var(--orange); font-weight: 700; font-size: 18px; }
  .credentials { font-size: 14px; font-weight: 600; }
  .role { color: var(--orange); font-weight: 700; font-size: 13px; }
  .contact-list { list-style: none; margin-top: 10px; font-size: 12.5px; }
  .contact-item { display: flex; align-items: center; gap: 7px; line-height: 1.35; }
  .contact-icon { width: 12px; height: 12px; fill: var(--orange); flex: none; }
</style>
</head>
<body>

<section class="card card-back card-textured" aria-label="Card back">
  <h2 class="practice-heading">AREAS OF PRACTICE:</h2>
  <ul class="practice-list">
    <li class="practice-area">
      <div class="practice-title">FAMILY LAW</div>
      <div class="practice-detail">Collaborative Practice</div>
      <div class="practice-detail">Meditation &amp; Negotiation</div>
      <div class="practice-detail">Intervention Orders</div>
    </li>
    <li class="practice-area">
      <div class="practice-title">CRIMINAL LAW</div>
    </li>
  </ul>
  <p class="service-region">MELBOURN<br>EASTERN AND BAYSIDE SUBURBS</p>
  <p class="website">www.Harrowgatelegal.com.au</p>
</section>

<section class="card card-front" aria-label="Card front">
  <div class="front-top">
    <div class="brand">
      <span class="brand-dot"></span>
      <span class="brand-name">Harrowgate Legal</span>
    </div>
    <ul class="values">
      <li>Experience</li>
      <li>Support</li>
      <li>Solutions</li>
    </ul>
  </div>
  <div class="accent-rule"></div>
  <div class="front-bottom card-textured">
    <div class="person-name">J. Marisa Thornbury</div>
    <div class="credentials">LLB (Hons) - Accredited Mediator</div>
    <div class="role">Principal Solicitor</div>
    <ul class="contact-list">
      <li class="contact-item">
        <svg class="contact-icon" viewBox="0 0 24 24" aria-hidden="true"><path d="M6.6 10.8a15.1 15.1 0 0 0 6.6 6.6l2.2-2.2a1 1 0 0 1 1-.25 11.4 11.4 0 0 0 3.6.57 1 1 0 0 1 1 1V20a1 1 0 0 1-1 1A17 17 0 0 1 3 4a1 1 0 0 1 1-1h3.5a1 1 0 0 1 1 1c0 1.25.2 2.45.57 3.6a1 1 0 0 1-.25 1z"/></svg>
        1300 Harrowgate (427 769)
      </li>
      <li class="contact-item">
        <svg class="contact-icon" viewBox="0 0 24 24" aria-hidden="true"><path d="M7 1h10a2 2 0 0 1 2 2v18a2 2 0 0 1-2 2H7a2 2 0 0 1-2-2V3a2 2 0 0 1 2-2zm0 4v13h10V5zm5 14.5a1 1 0 1 0 0 2 1 1 0 0 0 0-2z"/></svg>
        0400 555 018
      </li>
      <li class="contact-item">
        <svg class="contact-icon" viewBox="0 0 24 24" aria-hidden="true"><path d="M2 5h20v14H2zm2 2v.5l8 5 8-5V7zm0 2.8V17h16V9.8l-8 5z"/></svg>
        marisa.thornbury@harrowgatelegal.com.au
      </li>
    </ul>
  </div>
</section>

</body>
</html>
```